Roles For Metrics - Job Board for Big Data Professionals

Hi all,

I need a design for a job board I'm kicking off that is focused on finding jobs and people that work in Data Analytics.

I've attached a fairly in depth design spec and wireframe giving a rough mockup. Please note that in the wireframe, the boxes are there to demonstrate orders of content. This is not to say that a lot of distinct content boxes will necessarily be the best way of presenting content.

I will be available on Chatterlink (marcus.wendholt) and email (w3ndh0lt@quillpost.net) and will give constant and clear feedback on the way.

Payment is not guaranteed yet. As soon as there are at least 5+ promising designs I will make this guaranteed.

Thanks
Marcus
Updates

Hi all

Please suspend all work on this project for the time being.

I am working closely with 1 designer who I will very likely accept their design.

I appreciate all the work you have put into this, but dont want to waste any more of your time.

Thanks
Marcus

Industry/Entity Type

Work

Requirements
Must have
• I'd like a clean, modern web design which has strong use of Typography. Strong use of a clear and consistent palette of colours.
Should not have
• Boxes with rounded edges

```html
<!DOCTYPE html>
<html lang="en">
<head>
<meta charset="utf-8">
<title>Roles For Metrics – Jobs</title>
<link href="https://fonts.googleapis.com/css2?family=Crimson+Pro:wght@400;600;700&family=Arimo:wght@400;700&family=Oswald:wght@500;600&display=swap" rel="stylesheet">
<style>
:root{
  --green:#86b24a;--green-dark:#6e9a36;--green-text:#8cb84f;
  --red:#c8423d;--red-soft:#e07a72;--yellow:#f2c230;
  --ink:#333;--muted:#666;--light:#999;--rule:#ddd;
  --panel:#6d6d6d;--panel-dark:#585858;--page:#f2f2f2;
  --contract:#e6bf45;--fulltime:#d9534f;--freelance:#c3237f;--intern:#74a83b;
  --serif:"Crimson Pro",Georgia,serif;--sans:"Arimo",Arial,sans-serif;
}
*{box-sizing:border-box;margin:0;padding:0}
html,body{width:1200px;height:1140px;overflow:hidden}
body{position:relative;background:var(--page);font-family:var(--sans);color:var(--ink);font-size:10px}
.abs{position:absolute}
.masthead-bg{left:0;top:0;width:1200px;height:112px;background:linear-gradient(#3a3a3a,#262626)}
.logo{left:213px;top:18px;font-family:var(--serif);font-size:38px;font-weight:400;color:#9cc35a;letter-spacing:.5px;white-space:nowrap}
.ad-top{left:627px;top:18px;width:381px;height:49px;background:linear-gradient(#fff,#e9e9e9);border:1px solid #ccc;display:flex;align-items:center;justify-content:center;font-family:var(--serif);font-size:36px;color:#d5d5d5;letter-spacing:2px;font-variant:small-caps}
.nav{left:192px;top:83px;width:816px;height:30px;background:linear-gradient(#94bf55,#7aa83f);display:flex}
.nav a{font-family:var(--serif);font-size:15px;font-weight:600;color:#fff;padding:0 16px;line-height:30px;text-decoration:none;white-space:nowrap}
.nav a.home{background:#6b9636}
.nav a.active{background:#fff;color:#444}
.subnav{left:192px;top:113px;width:816px;height:26px;background:linear-gradient(#fafafa,#e4e4e4);display:flex;padding-left:18px}
.subnav a{font-family:var(--serif);font-size:11.5px;color:#444;line-height:26px;margin-right:26px;text-decoration:none;white-space:nowrap}
.panel{left:192px;top:139px;width:816px;height:124px;background:linear-gradient(#7a7a7a,var(--panel-dark));display:flex}
.panel-col{position:relative;height:100%}
.panel-col.login{width:408px;border-right:1px solid #4d4d4d}
.panel-col.search{width:408px;border-left:1px solid #8a8a8a}
.panel h2{position:absolute;top:11px;font-family:var(--serif);font-size:18px;font-weight:600;color:#fff}
.field{position:absolute;height:20px;background:#fff;border:1px solid #ccc;font-size:8.5px;color:#999;padding:5px 9px}
.btn-green{position:absolute;background:linear-gradient(#9ccb5b,#6e9a36);color:#fff;font-family:var(--serif);font-weight:700;font-size:10px;padding:3px 8px;border:1px solid #5c8229}
.btn-yellow{position:absolute;background:linear-gradient(#ffd84c,#e8b41d);color:#6b4b00;font-family:var(--serif);font-weight:700;font-size:10px;padding:3px 8px}
.small-white{position:absolute;font-size:8.5px;color:#eee;white-space:nowrap}
.radio{display:inline-block;width:10px;height:10px;border-radius:50%;background:#fff;vertical-align:-2px;margin-right:4px}
.radio.on{border:3px solid #8cb84f}
.content{left:192px;top:263px;width:816px;height:630px;background:#fff;border:1px solid #e2e2e2}
.section-title{font-family:var(--serif);font-size:16px;font-weight:600;color:#444}
.jobs{left:210px;top:302px;width:522px;height:504px;border:1px solid #ddd;border-top:none}
.filters{height:36px;background:linear-gradient(#fff,#eee);border-top:1px solid #ddd;border-bottom:1px solid #ddd;display:flex;align-items:center;padding-left:8px}
.select{width:120px;height:22px;border:1px solid #aaa;background:#fff;font-size:9.5px;color:#444;padding:5px 11px;position:relative}
.select::after{content:"";position:absolute;right:0;top:0;width:22px;height:20px;background:#5a5a5a}
.select::before{content:"";position:absolute;right:7px;top:8px;border:4px solid transparent;border-top-color:#fff;z-index:1}
.check{font-size:9.5px;color:#444;margin-left:15px}
.box{display:inline-block;width:8px;height:8px;border:1px solid #bbb;background:#fff;margin-right:3px;vertical-align:-1px;position:relative}
.box.on::after{content:"";position:absolute;left:1px;top:-2px;width:3px;height:6px;border:solid var(--red);border-width:0 2px 2px 0;transform:rotate(40deg)}
.job{height:46px;border-bottom:1px solid #e3e3e3;position:relative}
.job.hi{background:#d4e5b8}
.tag{position:absolute;left:16px;top:12px;width:74px;height:20px;font-size:10px;font-weight:700;line-height:20px;padding-left:12px;color:#fff;clip-path:polygon(0 0,100% 0,92% 50%,100% 100%,0 100%)}
.tag.contract{background:var(--contract);color:#5a4300}
.tag.full{background:var(--fulltime)}
.tag.free{background:var(--freelance)}
.tag.intern{background:var(--intern);color:#213d05}
.job-title{position:absolute;left:98px;top:11px;font-size:9.5px;font-weight:700;color:var(--green-text);white-space:nowrap}
.job-co{position:absolute;left:98px;top:25px;font-size:8.5px;color:#888;white-space:nowrap}
.job-co b{color:#555}
.job-city{position:absolute;left:391px;top:12px;font-size:9.5px;font-weight:700;color:var(--red)}
.job-region{position:absolute;left:391px;top:26px;font-size:8.5px;color:#666;white-space:nowrap}
.pager{left:210px;top:780px;width:522px;height:26px;background:linear-gradient(#94bf55,#76a33c);display:flex;align-items:center;padding-left:16px;font-size:8.5px;color:#fff}
.pager span{margin-right:12px}
.pager .cur{background:#fff;color:#444;padding:2px 5px;margin-left:-5px;margin-right:7px}
.partners{left:210px;top:848px;width:782px;height:28px;display:flex;align-items:center}
.partners .arrow{width:17px;height:17px;border-radius:50%;background:var(--red);flex:none}
.partners .names{flex:1;display:flex;justify-content:space-around;font-family:var(--serif);font-size:13px;font-weight:600;color:#888}
.sidebar{left:754px;top:281px;width:235px;height:412px;background:#f1f1f1;border:1px solid #ddd}
.resume-banner{left:754px;top:281px;width:235px;height:99px;background:linear-gradient(#e8837b,#c9443e)}
.resume-pill{left:787px;top:298px;width:178px;height:50px;border-radius:25px;background:linear-gradient(#ffd33a,#f2a81a);border:3px solid #f4cf6d;font-family:"Oswald",sans-serif;font-weight:600;font-size:19px;color:#c1271f;text-align:center;line-height:44px;white-space:nowrap;overflow:hidden}
.resume-sub{left:811px;top:358px;font-size:8.5px;color:#fff;white-space:nowrap}
.side-h{font-family:var(--serif);font-size:13px;font-weight:600;color:#444}
.bullets{list-style:none}
.bullets li{position:relative;padding-left:20px;font-size:8.5px;color:#666;line-height:11px;border-bottom:1px solid #dcdcdc;padding-bottom:6px;margin-bottom:7px}
.bullets li::before{content:"";position:absolute;left:3px;top:2px;width:7px;height:7px;border-radius:50%;background:var(--red)}
.footer-bg{left:0;top:911px;width:1200px;height:229px;background:linear-gradient(#333,#222)}
.foot-h{font-family:var(--serif);font-size:15px;font-weight:700;color:var(--green-text);white-space:nowrap}
.foot-list{list-style:none;border-left:1px solid #888}
.foot-list li{font-size:10px;color:#ddd;height:22.6px;padding-left:14px;position:relative;white-space:nowrap}
.foot-list li::before{content:"";position:absolute;left:0;top:6px;width:9px;border-top:1px solid #888}
.social li{list-style:none;font-size:10px;color:#ddd;height:22px;white-space:nowrap}
.social i{display:inline-block;width:12px;height:12px;margin-right:6px;vertical-align:-2px}
.tweet{font-size:10px;color:#fff;line-height:15.5px}
.ad-foot{left:756px;top:905px;width:245px;height:203px;background:#fff;text-align:center}
.ad-foot .big{font-family:var(--serif);font-size:36px;color:#d0d0d0;line-height:40px;margin-top:50px;font-variant:small-caps}
.ad-foot .cap{font-size:12px;color:#bbb;margin-top:12px}
</style>
</head>
<body>
<div class="abs masthead-bg" role="img" aria-label="Dark mosaic of portrait photographs"></div>
<div class="abs logo">Roles For Metrics</div>
<div class="abs ad-top">Ad Space</div>

<nav class="abs nav">
  <a class="home">Home</a><a>About Us</a><a class="active">Jobs</a><a>Account</a><a>Register</a><a>News &amp; Insight</a><a>Graduates</a><a>Recruiters</a>
</nav>
<nav class="abs subnav">
  <a>Advanced Job Search</a><a>Companies</a><a>Account</a><a>Login</a><a>Post Resume</a><a>Alerts</a><a>Settings</a>
</nav>

<section class="abs panel">
  <div class="panel-col login">
    <h2 style="left:18px">Login</h2>
    <div class="field" style="left:18px;top:48px;width:163px">Username</div>
    <div class="field" style="left:193px;top:48px;width:163px">Password</div>
    <div class="btn-green" style="left:18px;top:80px">SIGN IN</div>
    <div class="small-white" style="left:86px;top:85px">Forgot your password ?</div>
  </div>
  <div class="panel-col search">
    <h2 style="left:55px">Quick Search</h2>
    <div class="field" style="left:56px;top:48px;width:163px">Keyword</div>
    <div class="field" style="left:235px;top:48px;width:163px">Location</div>
    <div class="small-white" style="left:58px;top:70px;font-family:var(--serif);font-size:12px;font-weight:700;color:#fff">Type</div>
    <div class="small-white" style="left:58px;top:89px"><span class="radio on"></span>Contract &nbsp;&nbsp;&nbsp;<span class="radio"></span>Permanent</div>
    <div class="btn-yellow" style="left:238px;top:84px">SEARCH</div>
    <div class="small-white" style="left:308px;top:89px;font-family:var(--serif);font-size:9.5px">Advanced Search</div>
  </div>
</section>

<main class="abs content"></main>
<h1 class="abs section-title" style="left:211px;top:278px">All Jobs</h1>

<section class="abs jobs">
  <div class="filters">
    <div class="select">Job Categories</div>
    <span class="check" style="margin-left:88px"><span class="box on"></span>Full-time</span>
    <span class="check"><span class="box on"></span>Contaract</span>
    <span class="check"><span class="box"></span>Freelance</span>
    <span class="check"><span class="box"></span>Internship</span>
  </div>
  <div class="job"><span class="tag contract">Contract</span><span class="job-title">Part Time Services Assignments</span><span class="job-co"><b>Brand|Solutions</b>: Business Development and|research</span><span class="job-city">Los Angeles</span><span class="job-region">California, United States</span></div>
  <div class="job hi"><span class="tag full">Full Time</span><span class="job-title" style="color:#2f4f10">Platform Validation Engineer</span><span class="job-co"><b>IME Lumora In</b>: (San Francisco, CA)</span><span class="job-city">London</span><span class="job-region">England, UnitedKingdom</span></div>
  <div class="job"><span class="tag contract">Contract</span><span class="job-title">Sr. Finance Manager</span><span class="job-co"><b>Investment Capital Group</b>: (Washington, DC)</span><span class="job-city">Los Angeles</span><span class="job-region">California, United States</span></div>
  <div class="job"><span class="tag free">Freelance</span><span class="job-title">Interactive/Web Designer</span><span class="job-co"><b>Hudson Street Media</b>:(New York, NY)</span><span class="job-city">London</span><span class="job-region">England, UnitedKingdom</span></div>
  <div class="job"><span class="tag intern">Internship</span><span class="job-title">Sr. Web Developer/Designer</span><span class="job-co"><b>Brand|Solutions</b>:Development and|research</span><span class="job-city">Los Angeles</span><span class="job-region">California, United States</span></div>
  <div class="job"><span class="tag full">Full Time</span><span class="job-title">Part Time Services Assignments</span><span class="job-co"><b>Investment Capital Group</b>: (Washington, DC)</span><span class="job-city">London</span><span class="job-region">England, UnitedKingdom</span></div>
  <div class="job"><span class="tag full">Full Time</span><span class="job-title">Part Time Services Assignments</span><span class="job-co"><b>IME Lumora In</b>: (San Francisco, CA)</span><span class="job-city">Los Angeles</span><span class="job-region">California, United States</span></div>
  <div class="job"><span class="tag free">Freelance</span><span class="job-title">Interactive/Web Designer</span><span class="job-co"><b>Hudson Street Media</b>:(New York, NY)</span><span class="job-city">London</span><span class="job-region">England, UnitedKingdom</span></div>
  <div class="job" style="border-bottom:none"><span class="tag intern">Internship</span><span class="job-title">Sr. Web Developer/Designer</span><span class="job-co"><b>Brand|Solutions</b>:Development and|research</span><span class="job-city">Los Angeles</span><span class="job-region">California, United States</span></div>
</section>

<nav class="abs pager">
  <svg width="12" height="10" style="margin-right:16px"><path d="M0 5 L6 0 V3 H12 V7 H6 V10 Z" fill="#fff"/></svg>
  <span>1</span><span>2</span><span>3</span><span>4</span><span>5</span><span>6</span><span class="cur">7</span><span>8</span><span>9</span><span>........</span><span>103</span><span>104</span><span>105</span><span>106</span>
  <svg width="12" height="10"><path d="M12 5 L6 0 V3 H0 V7 H6 V10 Z" fill="#fff"/></svg>
</nav>

<h2 class="abs section-title" style="left:211px;top:818px">Featured Partners</h2>
<div class="abs partners">
  <span class="arrow"></span>
  <div class="names"><span>Swiftmark</span><span>Civic'08</span><span>Tunebox</span><span>Ledgerly</span><span>Orchard</span><span>MuSA</span><span>Peakcast</span><span>VELLANO</span><span>Pixelforge</span><span>Civic'08</span><span>Orchard</span><span>MuSA</span></div>
  <span class="arrow"></span>
</div>

<aside class="abs sidebar"></aside>
<div class="abs resume-banner"></div>
<div class="abs resume-pill">POST YOUR RESUME</div>
<svg class="abs" style="left:765px;top:320px" width="40" height="46"><path d="M30 4 Q2 8 4 28 Q6 42 34 42" fill="none" stroke="#fff" stroke-width="1.5"/><path d="M26 1 L33 4 L27 9" fill="none" stroke="#fff" stroke-width="1.5"/></svg>
<div class="abs resume-sub">Click here and bost your resume</div>

<div class="abs" style="left:769px;top:390px;width:207px">
  <div style="display:flex;justify-content:space-between;border-bottom:1px solid #ccc;padding-bottom:5px;margin-bottom:10px"><span class="side-h">Latest News</span><span style="font-size:8px;color:var(--red);text-decoration:underline;margin-top:4px">More articles</span></div>
  <ul class="bullets">
    <li>Your openings are featured in one of the top 20 blogs of the world</li>
    <li>Your credits are valid for unlimited time</li>
    <li>You can change your job postings whenever you like</li>
    <li>Job postings are online immediately</li>
  </ul>
</div>
<div class="abs" style="left:763px;top:545px;width:216px">
  <div class="side-h" style="border-bottom:1px solid #ccc;padding-bottom:5px">Subscribe for job Alerts</div>
  <p style="font-size:8.5px;color:#555;line-height:11px;margin-top:7px">Lorem Ipsum is simply dummy text of the printing and typesetting industry.</p>
  <div style="display:flex;margin-top:10px"><span style="font-size:10px;color:var(--red);margin:4px 0 0 1px;width:44px">Email</span><span style="width:171px;height:20px;background:#fff;border:1px solid #ccc"></span></div>
  <div style="margin:7px 0 0 44px;width:65px;height:20px;background:#555;color:#fff;font-family:var(--serif);font-size:10px;text-align:center;line-height:20px">SUBMIT</div>
</div>

<div class="abs" style="left:755px;top:714px;width:233px">
  <div class="side-h" style="border-bottom:1px solid #ccc;padding-bottom:5px;margin-bottom:10px">Why Roles For Metrics?</div>
  <ul class="bullets">
    <li style="border:none">Jobseekers sub-headline, with three listed bullet points and "Register to</li>
    <li style="border:none">Recruiters sub-headline, with three listed bullet points and "Register to</li>
  </ul>
</div>

<footer>
  <div class="abs footer-bg" role="img" aria-label="Dark mosaic of portrait photographs"></div>
  <div class="abs" style="left:205px;top:929px">
    <div class="foot-h">Browse Company</div>
    <ul class="foot-list" style="margin:10px 0 0 5px">
      <li>Home</li><li>Jobs</li><li>Account Register</li><li>News &amp; Insight</li><li>Graduates</li><li>Recruiters</li><li>About</li>
    </ul>
  </div>
  <div class="abs" style="left:368px;top:929px">
    <div class="foot-h">Social Sharing</div>
    <ul class="social" style="margin-top:12px">
      <li><i style="background:#3aa0d8"></i>Follow us on Chirpline</li>
      <li><i style="background:#f08a1c"></i>Post RSS Feeds</li>
    </ul>
  </div>
  <div class="abs" style="left:536px;top:930px;width:200px">
    <div class="foot-h">Consulting on Chirpline</div>
    <p class="tweet" style="margin-top:10px"><span style="color:var(--green-text)">Yesterday by harbor consulting</span><br>I've nothing but great things to say about @Mailcrest. Lorem ipsum dolor sit amet, consectetur no urna adipiscing elit. Nullam sit amet urna Lorem ipsum dolor<br><i style="color:var(--green-text);font-size:8.5px">Posted 15 hours ago</i></p>
  </div>
  <div class="abs ad-foot"><div class="big">Ad<br>Space</div><div class="cap">Featured Partners AD &nbsp;300px 250px</div></div>
</footer>
</body>
</html>
```